Come Play With Us!!! We are the Elite

We need a hiring flyer to hand out to potential recruits.
Please promote our social pages.
Something attractive, and informative with calls to action to contact us.
Please promote for people to follow us on social media.
We would like to list the following advantages to work here:
• Industry Leading Compensation
• Structured Career Advancement
• Safe Work Environment
• Work Promise Policy (Full Time Staff)
• Health & Dental Benefits
• Paid Training Programs
• Paid Clothing Allowance
• Paid Boot Allowance
• Positive Culture
• Progressive Culture
• Equal Opportunity Employer
• Veteran Friendly Employer
• New Equipment
• Paid Leadership Training
• Transparent Communication
• Community Focused
• Prestigious Clientele
• Local Work
• Focused on using industry leading tech
• Tool Purchase Program
• Family Atmosphere
• Team Events (Sports games, Lunches, Get togethers, Etc)
• Work Life balance
• Daily On Call Snow Pay
- Sick Pay
- Positive reputation
• Bonus’s available:
o Winter Shift Premium
o Referral Bonus
o Project Incentives
Current Positions open:
- Winter Crew Members
- Salt Truck Driver/Operator (AZ/DZ/AR)
- Winter Equipment Operators
- Construction Foreperson
Landscape and Construction

```html
<!DOCTYPE html>
<html lang="en">
<head>
<meta charset="utf-8">
<title>Ridgeline Contracting Group – We Are Hiring</title>
<link href="https://fonts.googleapis.com/css2?family=Bebas+Neue&family=Roboto+Condensed:wght@300;400&family=Montserrat:wght@400;600&display=swap" rel="stylesheet">
<style>
  :root {
    --page-bg: #5b5b5b;
    --green-dark: #0c8546;
    --green-mid: #3da544;
    --green-light: #6dbb45;
    --lime: #c9df6c;
    --paper: #f1f1f1;
    --ink: #3c3c3c;
    --footer-grey: #646464;
    --white: #ffffff;
  }
  html, body { margin: 0; padding: 0; overflow: hidden; }
  body {
    width: 1200px; height: 1200px;
    background: var(--page-bg);
    display: flex; align-items: center; justify-content: center;
  }
  .flyer { width: 820px; height: 1160px; display: block; }
  .headline { font-family: "Bebas Neue", "Oswald", sans-serif; }
  .headline-solid { fill: var(--white); font-size: 104px; }
  .headline-outline { fill: none; stroke: var(--white); stroke-width: 3; font-size: 178px; }
  .headline-tag { fill: var(--lime); font-size: 84px; }
  .section-title { font-family: "Bebas Neue", sans-serif; fill: var(--white); font-size: 30px; letter-spacing: .5px; }
  .position-item { font-family: "Roboto Condensed", sans-serif; font-weight: 300; fill: var(--white); font-size: 20px; }
  .benefit-line { font-family: "Roboto Condensed", sans-serif; font-weight: 300; fill: var(--white); font-size: 17px; }
  .brand-name { font-family: "Montserrat", sans-serif; font-weight: 400; fill: var(--ink); font-size: 26px; letter-spacing: 2px; }
  .contact-text { font-family: "Montserrat", sans-serif; font-weight: 400; fill: var(--white); font-size: 17px; }
  .follow-label { font-family: "Montserrat", sans-serif; font-weight: 600; fill: var(--white); font-size: 19px; }
  .photo-gap { fill: none; stroke: var(--white); stroke-width: 7; stroke-linejoin: miter; }
</style>
</head>
<body>
<svg class="flyer" viewBox="0 0 1026 1452" xmlns="http://www.w3.org/2000/svg" aria-label="Hiring flyer">
  <defs>
    <linearGradient id="bgGreen" x1="0" y1="0" x2="1" y2="1">
      <stop offset="0" stop-color="#6dbb45"/>
      <stop offset="0.55" stop-color="#2c9a47"/>
      <stop offset="1" stop-color="#0c8546"/>
    </linearGradient>
    <linearGradient id="facetLight" x1="0" y1="0" x2="1" y2="1">
      <stop offset="0" stop-color="#6fbe46"/>
      <stop offset="1" stop-color="#1a8c47"/>
    </linearGradient>
    <linearGradient id="paperGrad" x1="0" y1="0" x2="1" y2="1">
      <stop offset="0" stop-color="#e6e6e6"/>
      <stop offset="1" stop-color="#f7f7f7"/>
    </linearGradient>
    <linearGradient id="photoCrew" x1="0" y1="0" x2="0" y2="1">
      <stop offset="0" stop-color="#a9b9c9"/><stop offset=".45" stop-color="#c9d94a"/><stop offset="1" stop-color="#6f8a48"/>
    </linearGradient>
    <linearGradient id="photoOrange" x1="0" y1="0" x2="1" y2="1">
      <stop offset="0" stop-color="#d8d3c8"/><stop offset=".5" stop-color="#e8601f"/><stop offset="1" stop-color="#9a4a22"/>
    </linearGradient>
    <linearGradient id="photoCab" x1="0" y1="0" x2="1" y2="1">
      <stop offset="0" stop-color="#9cc0cc"/><stop offset=".5" stop-color="#b8c45a"/><stop offset="1" stop-color="#3b3b3b"/>
    </linearGradient>
    <linearGradient id="photoWoman" x1="0" y1="0" x2="1" y2="1">
      <stop offset="0" stop-color="#8a7355"/><stop offset=".5" stop-color="#2a3444"/><stop offset="1" stop-color="#6f6a5a"/>
    </linearGradient>
    <linearGradient id="photoWorker" x1="0" y1="0" x2="1" y2="1">
      <stop offset="0" stop-color="#7d8b5a"/><stop offset=".5" stop-color="#c9957a"/><stop offset="1" stop-color="#26303f"/>
    </linearGradient>
    <linearGradient id="photoBeard" x1="0" y1="0" x2="1" y2="1">
      <stop offset="0" stop-color="#8d8f86"/><stop offset=".5" stop-color="#b98a6c"/><stop offset="1" stop-color="#2b2b2b"/>
    </linearGradient>
    <linearGradient id="photoTools" x1="0" y1="0" x2="1" y2="1">
      <stop offset="0" stop-color="#5a6b40"/><stop offset=".6" stop-color="#2d2d2d"/><stop offset="1" stop-color="#a08f6b"/>
    </linearGradient>
  </defs>

  <!-- base -->
  <rect class="sheet" width="1026" height="1452" fill="url(#bgGreen)"/>
  <polygon class="facet-right" points="1026,845 770,600 1026,600" fill="#1f9047" opacity=".6"/>
  <polygon class="facet-mid" points="770,600 1026,845 840,1030 560,840" fill="url(#facetLight)" opacity=".55"/>

  <!-- top-left paper panel -->
  <polygon class="paper-panel" points="0,0 180,0 400,230 175,455 0,300" fill="url(#paperGrad)"/>

  <!-- photo collage -->
  <g class="photo-collage">
    <polygon role="img" aria-label="Photo: smiling crew member in a cap holding a coffee" points="0,300 240,520 80,690 0,615" fill="url(#photoWoman)"/>
    <polygon role="img" aria-label="Photo: three crew members in high-visibility vests on a residential street" points="400,230 590,410 355,650 170,455" fill="url(#photoCrew)"/>
    <polygon role="img" aria-label="Photo: smiling worker in orange hoodie and safety vest beside a company sign" points="590,410 770,600 540,840 355,650" fill="url(#photoOrange)"/>
    <polygon role="img" aria-label="Photo: operator at the controls inside an equipment cab" points="240,520 540,840 420,975 80,690" fill="url(#photoCab)"/>
    <polygon role="img" aria-label="Photo: smiling young worker outdoors" points="0,615 80,690 190,815 0,1005" fill="url(#photoWorker)"/>
    <polygon role="img" aria-label="Photo: bearded worker in a cap smiling at a job site" points="190,815 420,975 380,1015 190,1205 0,1005" fill="url(#photoBeard)"/>
    <polygon role="img" aria-label="Photo: crew member working with power tools in a garden bed" points="0,1005 190,1205 0,1370" fill="url(#photoTools)"/>
    <polyline class="photo-gap" points="0,300 240,520 80,690"/>
    <polyline class="photo-gap" points="175,455 590,410"/>
    <polyline class="photo-gap" points="355,650 590,410"/>
    <polyline class="photo-gap" points="240,520 540,840"/>
    <polyline class="photo-gap" points="80,690 420,975"/>
    <polyline class="photo-gap" points="190,815 0,1005"/>
    <polyline class="photo-gap" points="190,815 380,1015"/>
    <polyline class="photo-gap" points="0,1005 190,1205"/>
    <polyline class="photo-gap" points="590,410 770,600"/>
  </g>

  <!-- lower facets and footer -->
  <polygon class="facet-bottom" points="0,1370 190,1205 380,1015 505,1452 0,1452" fill="url(#facetLight)"/>
  <polygon class="footer-band" points="370,1298 1026,1298 1026,1452 505,1452" fill="var(--footer-grey)"/>

  <!-- brand -->
  <g class="brand">
    <circle cx="100" cy="225" r="52" fill="none" stroke="var(--ink)" stroke-width="7"/>
    <text class="brand-name" x="168" y="208">RIDGELINE</text>
    <text class="brand-name" x="168" y="238">CONTRACTING</text>
    <text class="brand-name" x="168" y="268">GROUP</text>
  </g>

  <!-- headline -->
  <g class="headline" text-anchor="end">
    <text class="headline-solid" x="962" y="230">WE ARE</text>
    <text class="headline-outline" x="962" y="368">HIRING!</text>
    <text class="headline-tag" x="962" y="440">COME PLAY</text>
    <text class="headline-tag" x="962" y="508">WITH US!!!</text>
  </g>

  <!-- positions -->
  <g class="positions">
    <text class="section-title" x="632" y="808">POSITIONS AVAILABLE</text>
    <line x1="632" y1="819" x2="958" y2="819" stroke="#8fcb7d" stroke-width="4"/>
    <line x1="632" y1="819" x2="852" y2="819" stroke="var(--green-dark)" stroke-width="5"/>
    <g class="position-list">
      <g transform="translate(643,844)"><circle r="11" fill="var(--white)"/><polygon points="-3,-6 7,0 -3,6" fill="var(--green-mid)"/></g>
      <text class="position-item" x="660" y="851">WINTER CREW MEMBERS</text>
      <g transform="translate(643,872)"><circle r="11" fill="var(--white)"/><polygon points="-3,-6 7,0 -3,6" fill="var(--green-mid)"/></g>
      <text class="position-item" x="660" y="879">SALT TRUCK DRIVER / OPERATOR</text>
      <text class="position-item" x="660" y="899">( AZ / DZ / AR )</text>
      <g transform="translate(643,916)"><circle r="11" fill="var(--white)"/><polygon points="-3,-6 7,0 -3,6" fill="var(--green-mid)"/></g>
      <text class="position-item" x="660" y="923">WINTER EQUIPMENT OPERATORS</text>
      <g transform="translate(643,945)"><circle r="11" fill="var(--white)"/><polygon points="-3,-6 7,0 -3,6" fill="var(--green-mid)"/></g>
      <text class="position-item" x="660" y="952">CONSTRUCTION FOREPERSON</text>
    </g>
  </g>

  <!-- benefits -->
  <g class="benefits">
    <text class="section-title" x="463" y="1013">BENEFITS</text>
    <line x1="463" y1="1024" x2="958" y2="1024" stroke="#8fcb7d" stroke-width="4"/>
    <line x1="463" y1="1024" x2="556" y2="1024" stroke="var(--green-dark)" stroke-width="5"/>
    <text class="benefit-line" x="455" y="1048">• Industry Leading Compensation • Structured Career Advancement • Safe Work</text>
    <text class="benefit-line" x="463" y="1070">Environment • Work Promise Policy (Full Time Staff) • Health &amp; Dental Benefits</text>
    <text class="benefit-line" x="455" y="1093">• Paid Training Programs • Paid Clothing Allowance • Paid Boot Allowance</text>
    <text class="benefit-line" x="455" y="1115">• Positive Culture • Progressive Culture • Equal Opportunity Employer • Veteran</text>
    <text class="benefit-line" x="463" y="1138">Friendly Employer • New Equipment • Paid Leadership Training • Transparent</text>
    <text class="benefit-line" x="463" y="1160">Communication • Community Focused • Prestigious Clientele • Local Work</text>
    <text class="benefit-line" x="455" y="1183">• Focused on using industry leading tech • Tool Purchase Program • Family</text>
    <text class="benefit-line" x="463" y="1205">Atmosphere • Work Life balance • Team Events (Sports games, Lunches,</text>
    <text class="benefit-line" x="463" y="1227">Get togethers, Etc) • Daily On Call Snow Pay (Sick Pay, Positive reputation)</text>
    <text class="benefit-line" x="455" y="1250">• Bonus’s available (Winter Shift Premium, Referral Bonus, Project Incentives)</text>
  </g>

  <!-- contact -->
  <g class="contact">
    <g class="icon-globe" fill="none" stroke="var(--white)" stroke-width="2">
      <circle cx="83" cy="1357" r="11"/>
      <ellipse cx="83" cy="1357" rx="5" ry="11"/>
      <line x1="72" y1="1357" x2="94" y2="1357"/>
    </g>
    <text class="contact-text" x="102" y="1363">www.ridgelinecontracting.com</text>
    <path class="icon-phone" d="M76 1380 q-6 6 -2 14 q5 9 13 12 l5 -5 l-6 -5 l-3 3 q-4 -3 -6 -7 l3 -3 z" fill="var(--white)"/>
    <text class="contact-text" x="102" y="1396">555-010-2847</text>
  </g>

  <g class="social">
    <text class="follow-label" x="447" y="1363">Follow Us :</text>
    <rect x="563" y="1347" width="20" height="20" rx="2" fill="var(--white)"/>
    <text class="contact-text" x="590" y="1363">ridgelinecontracting</text>
    <circle cx="802" cy="1357" r="10" fill="var(--white)"/>
    <text class="contact-text" x="818" y="1363">RidgelineCrew</text>
    <circle cx="573" cy="1390" r="10" fill="none" stroke="var(--white)" stroke-width="2"/>
    <text class="contact-text" x="590" y="1396">ridgeline_contracting</text>
  </g>
</svg>
</body>
</html>
```